Need Business cards

Im a new realtor and already have a logo. I would like to purchase a Business card design that catches customer's attention, its creative, and modern.

Marisol Quintero
Realtor ®
(555) 318 4027
marisolqtrhomes@brindlemail.com

Target Market(s)

investors, buyers and seller, property management

Industry/Entity Type

real estate,

Contact Information for Business Card

Marisol Quintero

Requirements
Must have
• BOTH LOGOS, WOULD LIKE TO SEE WITH DIFFERENT OPTIONS WITH EITHER PICTURE

```html
<!DOCTYPE html>
<html lang="en">
<head>
<meta charset="utf-8">
<title>Marisol Quintero – Business Card</title>
<link href="https://fonts.googleapis.com/css2?family=Playfair+Display:wght@400&family=Libre+Baskerville&family=Caveat:wght@400&family=Montserrat:wght@500;700&display=swap" rel="stylesheet">
<style>
  :root {
    --backdrop: #8c8c8c;
    --card-white: #ffffff;
    --back-light: #eef1f4;
    --back-edge: #d2d9e1;
    --name-tan: #efd3a3;
    --ink: #1d1d1d;
    --ink-soft: #3a3a3a;
    --icon-grey: #9a9a9a;
    --gold: #c4a03a;
    --brand-blue: #3c7bd0;
  }
  * { margin: 0; padding: 0; box-sizing: border-box; }
  html, body {
    width: 1200px; height: 1200px; overflow: hidden;
    background: var(--backdrop);
  }
  .canvas {
    width: 1200px; height: 1200px;
    display: flex; flex-direction: column; align-items: center; justify-content: center;
    gap: 60px;
  }
  .card {
    position: relative;
    width: 760px; height: 433px;
    overflow: hidden;
    box-shadow: 0 6px 18px rgba(0,0,0,.25);
  }
  /* Front */
  .card-front { background: var(--card-white); }
  .portrait {
    position: absolute; left: 14px; top: 26px; width: 340px; height: 407px;
    background: radial-gradient(ellipse at 50% 35%, #c9a987 0%, #e6cfa5 45%, #f3e4c4 75%, #ffffff 100%);
    border-radius: 44% 44% 0 0;
  }
  .agent-name {
    position: absolute; left: 360px; top: 80px;
    font-family: "Playfair Display", serif; font-weight: 400;
    font-size: 76px; line-height: 0.86; color: var(--name-tan);
    letter-spacing: -1px; white-space: nowrap;
  }
  .agent-title {
    position: absolute; left: 420px; top: 222px;
    font-family: "Caveat", cursive; font-weight: 400;
    font-size: 32px; line-height: 1; color: var(--ink);
    white-space: nowrap;
  }
  .contact {
    position: absolute; left: 370px; top: 334px;
    list-style: none;
    font-family: "Libre Baskerville", serif; font-size: 16px; color: var(--ink-soft);
    white-space: nowrap;
  }
  .contact li { display: flex; align-items: center; gap: 10px; height: 28px; }
  .contact svg { width: 20px; height: 20px; flex: none; }
  /* Back */
  .card-back {
    background: radial-gradient(ellipse at 50% 50%, var(--back-light) 0%, #e4e9ee 55%, var(--back-edge) 100%);
  }
  .agent-mark, .brokerage-mark {
    position: absolute; top: 50%; transform: translateY(-50%);
    display: flex; align-items: center; gap: 12px;
    font-family: "Montserrat", sans-serif; white-space: nowrap;
  }
  .agent-mark { left: 80px; font-weight: 500; font-size: 18px; letter-spacing: 1px; color: var(--gold); }
  .agent-mark .mark-square { width: 22px; height: 22px; background: var(--gold); }
  .brokerage-mark { left: 360px; font-weight: 700; font-size: 30px; letter-spacing: 1px; color: var(--brand-blue); }
  .brokerage-mark .mark-square { width: 26px; height: 26px; background: var(--brand-blue); }
</style>
</head>
<body>
<main class="canvas">
  <section class="card card-front">
    <div class="portrait" role="img" aria-label="Portrait photo of the realtor in a cream blazer"></div>
    <h1 class="agent-name">Marisol<br>Quintero</h1>
    <p class="agent-title">Real Estate Advisor</p>
    <ul class="contact">
      <li>
        <svg viewBox="0 0 24 24" fill="none" stroke="var(--icon-grey)" stroke-width="1.4"><path d="M6 3l3 4-2 2c1 3 4 6 7 7l2-2 4 3-2 3c-8 0-15-7-15-15z"/></svg>
        (555) 318 4027
      </li>
      <li>
        <svg viewBox="0 0 24 24" fill="none" stroke="var(--icon-grey)" stroke-width="1.4"><rect x="3" y="6" width="18" height="12"/><path d="M3 6l9 7 9-7"/></svg>
        marisolqtrhomes@brindlemail.com
      </li>
    </ul>
  </section>

  <section class="card card-back">
    <div class="agent-mark"><span class="mark-square"></span>MARISOL QUINTERO</div>
    <div class="brokerage-mark"><span class="mark-square"></span>STRIDEWELL REALTY</div>
  </section>
</main>
</body>
</html>
```